Commercial photographer, UAV drone photography & 360 walk-through visuals

I need a business card design that is minimalist but yet pretentiously creative. My target market are architects, designers, advertising agents and marketing managers. It is important to stress that though I am asking for a minimalist design it needs to have creative impact.

Target Market(s)

Architects, interiors designers, web-designers, artists

Contact Information for Business Card

Include my name, mobile [cell] number, email, web page and the company logo. Do not to include a postal address.

Colors

Designer to choose colors to be used in the design.

Requirements
Must have
• The following information is to be included:
• Miles Perrow
• Photographer
• m: 07812 593174
• e: miles@mpframeworks.co.uk
• w: mpframeworks.co.uk

```html
<!DOCTYPE html>
<html lang="en">
<head>
<meta charset="utf-8">
<title>MP Frameworks — Business Card</title>
<link href="https://fonts.googleapis.com/css2?family=Jost:wght@400&display=swap" rel="stylesheet">
<style>
  :root {
    --backdrop: #7fd0d8;
    --card: #fbfbf9;
    --ink: #111111;
  }
  html, body {
    margin: 0;
    padding: 0;
    width: 1200px;
    height: 1000px;
    overflow: hidden;
    background: var(--backdrop);
    font-family: "Jost", sans-serif;
    color: var(--ink);
  }
  .canvas {
    position: relative;
    width: 1200px;
    height: 1000px;
  }
  .card {
    position: absolute;
    left: 297px;
    width: 607px;
    height: 348px;
    background: var(--card);
  }
  .card--front { top: 110px; }
  .card--back  { top: 515px; }

  .brand {
    position: absolute;
    left: 0;
    right: 0;
    top: 122px;
    display: flex;
    align-items: center;
    justify-content: center;
    gap: 22px;
  }
  .brand__dot {
    width: 22px;
    height: 22px;
    border-radius: 50%;
    background: var(--ink);
  }
  .brand__name {
    font-size: 50px;
    font-weight: 400;
    letter-spacing: 3px;
    line-height: 1;
    text-transform: uppercase;
  }

  .identity {
    position: absolute;
    left: 170px;
    top: 118px;
    display: flex;
    align-items: center;
    gap: 22px;
  }
  .identity__dot {
    width: 16px;
    height: 16px;
    border-radius: 50%;
    background: var(--ink);
  }
  .identity__text {
    text-align: center;
    text-transform: uppercase;
    font-size: 25px;
    line-height: 32px;
    letter-spacing: 1px;
  }

  .contact {
    position: absolute;
    left: 0;
    right: 0;
    top: 303px;
    text-align: center;
    font-size: 15.5px;
    letter-spacing: 1px;
    text-transform: uppercase;
  }
  .contact__sep { margin: 0 8px; }
</style>
</head>
<body>
<main class="canvas">
  <section class="card card--front" aria-label="Card front">
    <div class="brand">
      <span class="brand__dot"></span>
      <span class="brand__name">MP Frameworks</span>
    </div>
  </section>

  <section class="card card--back" aria-label="Card back">
    <div class="identity">
      <span class="identity__dot"></span>
      <div class="identity__text">
        <div class="identity__name">Miles Perrow</div>
        <div class="identity__role">Photographer</div>
      </div>
    </div>
    <p class="contact">
      07812 593174<span class="contact__sep">|</span>miles@mpframeworks.co.uk<span class="contact__sep">|</span>mpframeworks.co.uk
    </p>
  </section>
</main>
</body>
</html>
```